QUORVIX - Sydney Based Technology Consultancy -Logo & Business Card design

Who are we?
-
Quorvix is an emerging and advanced technology consulting and professional services business based in Sydney, Australia. Quorvix specialising in increasing value to organisations through the effective use of current and emerging technologies, ensuring that technology is a sustainable catalyst to attaining stated business goals.

We pride ourselves in challenging the norm.

What do we want?
-
We are looking to update our "Brand" we already have a simple “home grown” logo and we are now looking for a new one, once we have this updated logo and businesses look and feel though the business card design we will refresh our website with the new logo and design thus updating the Companies overall look at feel.

Our current site is www.quorvix-example.net.au is a very basic wordpress site and we will be updating it once we have the new logo and designs done

Our initial thoughts on the new Quorvix identity are
• Logo Concept
- One of the key things is obviously the 8
- I was thinking that a logo that had 8 as the core of the logo would be cool,
- Almost like having a “ring” or hoop that is twisted to form an 8 with different services scribed on the inside.
- So we would have a Large 8 and the inside would have ring each service or section engraved.

• Brand / web Feel
- Simple
- Professional
- Innovative
- Clear
- Destination
- Unique
- Impartial
- Safe
- Leading edge
- Familiar

- Emerging technologies
- White and ice / glacier blue
- The familiar feel of the Brindle web site
- Embedded specialist Video clips

• Portfolio of Services
- Quorvix – A smart place for Smart people
- Quorvix – we provide the process to take ideas from awareness to reality
- Focus should be on the brand quality consistent clear local knowledge with regional, national, theatre and global presence

Access to Specialists
- Emerging technologies
- Sustainability
- Collaboration
- Data centre
- Virtualisation

• Adjacent ideas under the one Brand
- Tembrosk – Enable Business Collaboration
- Plinsk – Infrastructure Virtualisation
- morvo - smart people and processes
- skandel - Emerging technologies
- brunhavel - business to technology integration
- tolpin - Smart Infrastructure
- yusk – Connected communities
- dwol - sustainability

Target Market(s)

Australia, New Zealand and Asia pacific organisations that are typically English speaking.
Markets
- IT & Technology partners
- Banking and Finance
- Health

Industry/Entity Type

Business

Requirements
Must have
• Logo
Business cards
Colour pallette
3D Logo
Nice to have
• Style guide
Designer who can also assist with new Wordpress design
Should not have
• we don't want cheap looking, overtly flashy or gimmicky logo.

```html
<!DOCTYPE html>
<html lang="en">
<head>
<meta charset="utf-8">
<title>Quorvix</title>
<link rel="stylesheet" href="https://fonts.googleapis.com/css2?family=Anton&display=swap">
<style>
  :root {
    --ink: #000000;
    --paper: #ffffff;
    --splatter-light: #f2f2f2;
    --splatter-mid: #d2d2d2;
  }
  html, body {
    margin: 0;
    padding: 0;
    width: 1200px;
    height: 771px;
    overflow: hidden;
    background: var(--paper);
  }
  .card {
    display: block;
    width: 1200px;
    height: 771px;
  }
  .band--ink { fill: var(--ink); }
  .wordmark {
    font-family: "Anton", "Oswald", sans-serif;
    font-size: 218px;
  }
  .wordmark--dark { fill: var(--ink); }
  .wordmark--light { fill: var(--paper); }
</style>
</head>
<body>
<svg class="card" viewBox="0 0 1200 771" xmlns="http://www.w3.org/2000/svg">
  <defs>
    <linearGradient id="splatter-tone" x1="0" y1="0" x2="1" y2="1">
      <stop offset="0" stop-color="var(--splatter-mid)"/>
      <stop offset="0.5" stop-color="var(--splatter-light)"/>
      <stop offset="1" stop-color="var(--splatter-mid)"/>
    </linearGradient>
    <clipPath id="upper-half"><rect x="0" y="0" width="1200" height="385"/></clipPath>
    <clipPath id="lower-half"><rect x="0" y="385" width="1200" height="386"/></clipPath>
  </defs>

  <rect class="band band--ink" x="0" y="0" width="1200" height="76"/>
  <rect class="band band--splatter" x="0" y="76" width="1200" height="309" fill="url(#splatter-tone)" role="img" aria-label="Grey paint splatter texture on white"/>
  <rect class="band band--ink" x="0" y="385" width="1200" height="310"/>
  <rect class="band band--splatter" x="0" y="695" width="1200" height="76" fill="url(#splatter-tone)" role="img" aria-label="Grey paint splatter texture on white"/>

  <g clip-path="url(#upper-half)">
    <text class="wordmark wordmark--dark" x="245" y="469" textLength="731" lengthAdjust="spacing">QUORVIX</text>
  </g>
  <g clip-path="url(#lower-half)" aria-hidden="true">
    <text class="wordmark wordmark--light" x="245" y="469" textLength="731" lengthAdjust="spacing">QUORVIX</text>
  </g>
</svg>
</body>
</html>
```